Web Design Project

8 page static website.
About us/What we stand for:
Forno Lucente CBD plans to make a huge splash in Sydney by being the first Italian pizza and pasta retail food outlet offering truly fresh, nutritious ingredients – herbs and vegetables are picked directly from the garden, pizzas are made with love in a fun filled atmosphere and a cutting edge brand strategy that promotes a happy lifestyle and reminds people that happiness and togetherness comes from sharing amazing food.
The best thing about Forno Lucente is that it offers consumers a choice to either choose from the enticing gluten free and vegetarian menu range to the more traditional pizza and pasta, we cater for their own tastes, this provides a distinct point of difference in the retail food market, as well as allowing consumers to have an endless range of choices without having to worry about the nutritional value.
Consumers have now become accustomed to a consistent brand experience which is setting increasingly high standards when it comes to food quality, taste and service.
We want to capitalise on the opportunity to create a strong, modern brand that promotes healthy lifestyle habits, sells fresh, wholesome ingredients, delivers
exceptional service in a fun filled atmosphere and appeals to a broad market.
Our business model is specifically pickup and delivery with a few seats and crates for eating in. It is for the time poor that still want to have a great tasting Italian experience with pizza and pasta within the quick service restaurant space. Takeaway, office catering and delivery will be a large percentage of our business.
Our philosophy at Forno Lucente is simple:
“Success is not a formula, it’s a recipe”.
Brand personality:
We are located in a laneway and basically the shop is a hole in the one. It looks like a restaurant you would see in Italy.
Modern Italian, contemporary, fun, rustic (Tico Taco, Brasa’d)
1 Aims of this website
• Emotionally connect with the target audience to reflect (“happiness and togetherness comes from sharing amazing food”)
• To entice people to order pizza
• To capture a mailing list
• To differentiate us from the low cost, low quality pizza
• To create a connection with the target audience, and promote word of mouth
2 Target audience(s)
• Male/Female
• 18-49
• Sydney CBD and Woolloomooloo
• Internet Savvy.
3. Contents/Functionality
www.crustwander.com.au – like the rustic brown in the website and the old washed out white colour through the font.
Target Market(s)
18-49 years old
City worker and resident
people that enjoy good food
Industry/Entity Type
Restaurant
Requirements
Must have
- Some splash of red and green to represent the italian theme.
Nice to have
- Please see http://www.brasad-example.com.au/Pages/locationmenu.aspx
This is how our takeaway menu looks like.

```html
<!DOCTYPE html>
<html lang="en">
<head>
<meta charset="utf-8">
<title>Forno Lucente – Home</title>
<link rel="stylesheet" href="https://fonts.googleapis.com/css2?family=Bebas+Neue&family=Oswald:wght@500;600&family=Arimo:wght@400&display=swap">
<style>
  :root {
    --parchment: #e9cfa2;
    --parchment-dark: #d7b47e;
    --cream: #fbf9f4;
    --panel: #8c7442;
    --panel-light: #a38b59;
    --ink: #2b2213;
    --footer-ink: #3b2e1a;
    --green: #3a9e1c;
    --red: #d2140f;
    --white: #ffffff;
    --brown-text: #5a4424;
  }
  * { box-sizing: border-box; margin: 0; padding: 0; }
  html, body { width: 1200px; height: 645px; overflow: hidden; }
  body {
    position: relative;
    background: radial-gradient(ellipse at 45% 40%, #f1dcb4 0%, var(--parchment) 45%, var(--parchment-dark) 100%);
    font-family: "Arimo", Arial, sans-serif;
    color: var(--ink);
  }
  .topbar {
    position: absolute; left: 0; top: 0; width: 1200px; height: 63px;
    background: var(--cream);
  }
  .logo-tab {
    position: absolute; left: 100px; top: 62px; width: 258px; height: 96px; z-index: 4;
  }
  .brand {
    position: absolute; left: 196px; top: 48px; width: 130px; z-index: 5;
    display: flex; align-items: center; gap: 8px;
    font-family: "Bebas Neue", sans-serif; font-size: 28px; line-height: 28px;
    color: var(--green);
  }
  .brand-dot { width: 16px; height: 16px; border-radius: 50%; background: var(--red); flex: none; }
  .brand-name { width: 100px; }
  .nav {
    position: absolute; left: 353px; top: 30px;
    display: flex; align-items: center; gap: 10px;
    font-family: "Oswald", sans-serif; font-weight: 600; font-size: 17px; text-transform: uppercase;
  }
  .nav a { color: #111; text-decoration: none; letter-spacing: -0.2px; }
  .nav a.is-active {
    background: var(--green); color: var(--white);
    border-radius: 9px; padding: 0 11px; line-height: 17px;
  }
  .nav .sep { width: 7px; height: 7px; border-radius: 50%; background: var(--red); margin: 0 4px; }
  .main-panel {
    position: absolute; left: 161px; top: 63px; width: 875px; height: 407px;
    background: linear-gradient(160deg, var(--panel-light), var(--panel) 60%);
    border: 3px solid var(--cream); border-top: none;
    border-radius: 0 0 12px 12px;
  }
  .photo { position: absolute; border-radius: 12px; overflow: hidden; }
  .hero { left: 172px; top: 75px; width: 659px; height: 230px;
    background: linear-gradient(120deg, #7a3a1e, #b8462a 40%, #6e8a3a 65%, #3a2a1a); }
  .hero-caption {
    position: absolute; left: 638px; top: 118px; width: 171px; height: 147px;
    background: rgba(30, 24, 16, 0.72);
    font-family: "Bebas Neue", sans-serif; color: var(--cream);
    font-size: 30px; line-height: 45px; text-align: center; padding: 5px 10px 0;
    white-space: nowrap;
  }
  .hero-caption span { display: block; border-bottom: 1px solid var(--cream); }
  .hero-caption span:last-child { border-bottom: none; }
  .email-club {
    left: 172px; top: 317px; width: 327px; height: 142px;
    background: linear-gradient(135deg, #3b3128, #1e1915);
  }
  .email-club h2 {
    position: absolute; left: 30px; top: 4px;
    font-family: "Bebas Neue", sans-serif; font-weight: 400; font-size: 32px; line-height: 32px; color: var(--white);
  }
  .email-club .sub {
    position: absolute; left: 120px; top: 35px;
    font-family: "Oswald", sans-serif; font-weight: 500; font-size: 9px; line-height: 10px; color: var(--white);
  }
  .email-club input {
    position: absolute; left: 45px; width: 246px; height: 23px;
    border: none; border-radius: 4px; background: var(--cream);
    font-family: "Arimo", Arial, sans-serif; font-size: 10px; padding: 0 7px; color: #333;
  }
  .email-club .join {
    position: absolute; left: 217px; top: 116px; width: 83px; height: 19px;
    border: none; border-radius: 6px;
    background: linear-gradient(#8ee04a, #3c9a12);
    font-family: "Oswald", sans-serif; font-weight: 600; font-size: 12px; color: #102a04;
  }
  .catering {
    left: 506px; top: 317px; width: 325px; height: 144px;
    background: linear-gradient(135deg, #4a3a3a, #8a6c6a 45%, #c9b6b2 75%, #5a4a48);
  }
  .catering-label {
    position: absolute; left: 590px; top: 369px; width: 231px; height: 39px;
    background: rgba(40, 28, 26, 0.72);
    font-family: "Bebas Neue", sans-serif; font-size: 30px; line-height: 40px;
    color: var(--cream); padding-left: 10px; white-space: nowrap;
  }
  .order-badge { position: absolute; left: 846px; top: 52px; width: 205px; height: 132px; }
  .order-now {
    position: absolute; left: 906px; top: 100px; width: 134px; text-align: center;
    font-family: "Bebas Neue", sans-serif; white-space: nowrap;
  }
  .order-now .label { font-size: 30px; color: var(--green); line-height: 30px; }
  .order-now .phone { font-size: 22px; color: var(--brown-text); line-height: 24px; }
  .intro {
    position: absolute; left: 843px; top: 205px; width: 173px; text-align: center;
    font-family: "Bebas Neue", sans-serif; font-size: 20px; line-height: 19px; color: var(--white);
  }
  .welcome {
    position: absolute; left: 845px; top: 377px; width: 167px; text-align: center;
    font-family: "Bebas Neue", sans-serif; font-size: 22px; line-height: 28px; color: var(--white);
    border-top: 1px solid var(--cream); border-bottom: 1px solid var(--cream);
    padding: 0 0 8px; white-space: nowrap;
  }
  .footer-line {
    position: absolute; right: 166px; font-size: 10.5px; color: var(--footer-ink);
    text-transform: uppercase; letter-spacing: 0.3px; white-space: nowrap;
  }
  .btn-download {
    position: absolute; top: 522px; height: 19px; border-radius: 10px;
    background: linear-gradient(#efe4d0, #b8a27e);
    font-family: "Oswald", sans-serif; font-weight: 500; font-size: 10.5px; line-height: 19px;
    color: #3a2c18; text-align: center; text-transform: uppercase; white-space: nowrap;
  }
  .follow {
    position: absolute; right: 258px; top: 522px;
    font-family: "Bebas Neue", sans-serif; font-size: 18px; line-height: 22px; color: var(--brown-text);
    white-space: nowrap;
  }
  .social { position: absolute; top: 513px; width: 37px; height: 37px; border-radius: 4px; }
  .social--one { left: 952px; background: #3a5aa0; }
  .social--two { left: 996px; background: #222; }
</style>
</head>
<body>
  <header class="topbar"></header>

  <nav class="nav">
    <a href="#" class="is-active">Home</a><span class="sep"></span>
    <a href="#">About Us</a><span class="sep"></span>
    <a href="#">Menu</a><span class="sep"></span>
    <a href="#">Contact Us</a>
  </nav>

  <main>
    <section class="main-panel"></section>
    <div class="photo hero" role="img" aria-label="Photo of a fresh pizza topped with rocket, tomatoes and shaved parmesan"></div>
    <div class="hero-caption"><span>Italian Fresh,</span><span>Authentic,</span><span>Delicious</span></div>

    <form class="photo email-club">
      <h2>Join Our Email Club</h2>
      <p class="sub">FOR MEMBER ONLY BENEFITS &amp; REWARDS</p>
      <input type="text" placeholder="Enter your name:" style="top:55px">
      <input type="email" placeholder="Enter your email address:" style="top:90px">
      <button class="join" type="button">Join now&gt;</button>
    </form>

    <div class="photo catering" role="img" aria-label="Photo of tiramisu desserts in glasses for corporate catering"></div>
    <div class="catering-label">Corporate Catering</div>

    <svg class="order-badge" viewBox="0 0 205 132" aria-hidden="true">
      <circle cx="30" cy="30" r="30" fill="#fbf9f4"/>
      <path d="M55 5 H170 A36 36 0 0 1 205 40 V70 A64 64 0 0 1 141 132 A64 64 0 0 1 80 80 V50 A30 30 0 0 1 55 5 Z" fill="#fbf9f4"/>
      <circle cx="30" cy="32" r="23" fill="none" stroke="#8c7442" stroke-width="2.5"/>
      <path d="M22 20 q-6 12 4 24 q6 6 14 6 l3-6 -6-4 -3 3 q-6-3 -8-11 l3-2 -2-7 z" fill="#8c7442"/>
      <rect x="87" y="14" width="27" height="34" fill="#3a9e1c"/>
      <rect x="114" y="14" width="27" height="34" fill="#ffffff"/>
      <rect x="141" y="14" width="27" height="34" fill="#d2140f"/>
      <rect x="87" y="14" width="81" height="34" fill="none" stroke="#5a4424" stroke-width="1"/>
    </svg>
    <div class="order-now"><div class="label">Order Now</div><div class="phone">(02) 9000 4182</div></div>

    <p class="intro">At Forno Lucente,<br>we have perfected the secret to fresh, authentic Italian pizza. Made only from the highest quality and freshest natural ingredients.</p>
    <p class="welcome">Welcome – Benvenuti<br>to Forno Lucente</p>
  </main>

  <svg class="logo-tab" viewBox="0 0 258 96" aria-hidden="true">
    <path d="M0 0 H258 C200 20 160 60 135 88 Q128 97 118 92 C80 60 40 20 0 0 Z" fill="#fbf9f4"/>
  </svg>
  <div class="brand"><span class="brand-dot"></span><span class="brand-name">Forno<br>Lucente</span></div>

  <footer>
    <p class="footer-line" style="top:486px">Copyright © Forno Lucente 2011 &nbsp;|&nbsp; Forno Lucente's Privacy Policy</p>
    <a class="btn-download" style="left:475px;width:117px">Download our menu</a>
    <a class="btn-download" style="left:605px;width:204px">Download our catering order form</a>
    <p class="follow">Follow us on:</p>
    <span class="social social--one" role="img" aria-label="Social network link"></span>
    <span class="social social--two" role="img" aria-label="Social network link"></span>
    <p class="footer-line" style="top:575px">All major credit cards accepted.</p>
    <p class="footer-line" style="top:609px">Address: Lucerna Lane, Sydney CBD NSW</p>
  </footer>
</body>
</html>
```